Design revision of an existing Executive Summary

Our company velmora is specialized in the field of performance engineering (load and performance testing as well as application performance monitoring). We are looking for a designer who could graphically "spice up" our current executive summary about our company velmora (www.velmora-it.example). Maybe it would be possible to incorporate a pic of our website (e.g. https://www.velmora-it.example/en/services/performance/) into this newly designed executive summary.

Attached you will find the current executive summary which should not change textually. It should just look fresher and more modern. Ideally, a visually appealing first / title page would precede the text.

```html
<!DOCTYPE html>
<html lang="en">
<head>
<meta charset="utf-8">
<title>velmora – Executive Summary Document</title>
<link href="https://fonts.googleapis.com/css2?family=Montserrat:wght@700;800&family=Questrial&display=swap" rel="stylesheet">
<style>
  :root{
    --ink:#111;
    --white:#fff;
    --cyan:#22b5ee;
    --navy-deep:#010134;
    --blue-mid:#14427f;
    --blue-services:#0b2b7c;
    --blue-contact:#133a6c;
    --blue-contact-edge:#1b4f8e;
    --strip-dark:#1b1b1b;
    --strip-light:#cfcfcf;
    --label-blue:#1d4f91;
  }
  *{margin:0;padding:0;box-sizing:border-box}
  html,body{width:847px;height:1200px;overflow:hidden;background:var(--white)}
  body{font-family:"Questrial",sans-serif;color:var(--ink)}
  .sheet{position:relative;width:847px;height:1200px;border:1px solid #333;overflow:hidden}
  .abs{position:absolute}
  .section-label{font-size:25px;letter-spacing:.6px;color:var(--ink)}

  /* Cover */
  .cover{left:103px;top:136px;width:629px;height:444px;overflow:hidden;border:1px solid #555}
  .cover-photo{position:absolute;inset:0;
    background:
      radial-gradient(ellipse 60% 22% at 20% 100%, rgba(200,40,70,.55), transparent 70%),
      linear-gradient(180deg,#8a8a8a 0%,#5f5f5f 25%,#3a3a3a 50%,#1f1f1f 75%,#2a1a1e 100%)}
  .cover-band{position:absolute;left:0;top:150px;width:629px;height:167px;background:rgba(20,20,20,.72)}
  .cover-title{position:absolute;left:30px;top:196px;font-family:"Montserrat",sans-serif;font-weight:800;
    font-size:31px;line-height:32px;color:var(--white)}
  .brand{position:absolute;left:467px;top:197px;font-size:25px;letter-spacing:1px;color:var(--white)}
  .brand-claim{position:absolute;left:467px;top:241px;font-size:10.5px;color:var(--white)}
  .cover-tagline{position:absolute;left:357px;top:400px;font-size:9.5px;font-style:italic;color:var(--white)}

  /* Summary */
  .panel{position:absolute}
  .panel h2{font-weight:400;font-size:13.5px;letter-spacing:.4px;color:var(--cyan);text-transform:uppercase}
  .panel p{font-size:8.3px;line-height:10.1px;color:var(--white);text-align:justify}
  .who{left:103px;top:658px;width:314px;height:143px;background:var(--navy-deep);padding:25px 24px 0 26px}
  .team{left:417px;top:658px;width:290px;height:143px;background:var(--blue-mid);padding:25px 24px 0 22px}
  .strip-dark{left:707px;top:658px;width:24px;height:277px;background:var(--strip-dark)}
  .services{left:103px;top:801px;width:604px;height:134px;background:var(--blue-services);padding:12px 0 0 26px}
  .services h2{margin-bottom:6px}
  .service{position:absolute;top:37px}
  .service h3{font-family:"Montserrat",sans-serif;font-weight:700;font-size:9.6px;color:var(--white);margin-bottom:2px}
  .service p{font-size:8.3px;line-height:10.1px}
  .svc-1{left:25px;width:170px}
  .svc-2{left:217px;width:172px}
  .svc-3{left:409px;width:172px}
  .svc-3 p{text-align:left}
  .svc-num{position:absolute;top:62px;font-family:"Montserrat",sans-serif;font-weight:800;font-size:46px;color:rgba(255,255,255,.05)}

  .customers{left:103px;top:935px;width:628px;height:81px;background:var(--white)}
  .customers h2{position:absolute;left:26px;top:10px;font-weight:400;font-size:13.5px;letter-spacing:.4px;color:var(--label-blue)}
  .client{position:absolute;top:36px;font-size:14px;display:flex;align-items:center;gap:4px;height:20px}
  .client .mark{width:20px;height:20px;background:#004a8c;display:inline-block}
  .client-1{left:36px;color:#d2232a}
  .client-2{left:128px;color:#555}
  .client-3{left:216px;color:#004a8c;top:32px}
  .client-3 .mark{width:20px;height:28px}
  .client-4{left:300px;color:#0b7fa0}
  .client-5{left:376px;color:#d8232a}
  .client-6{left:460px;color:#1a9a2a}
  .client-6 .mark{width:8px;height:8px;background:#37d43a}

  .contact{left:103px;top:1016px;width:604px;height:86px;background:var(--blue-contact);color:var(--white);text-align:center}
  .contact-edge{left:103px;top:1016px;width:16px;height:86px;background:var(--blue-contact-edge)}
  .strip-light{left:707px;top:1016px;width:24px;height:86px;background:var(--strip-light)}
  .contact h2{position:absolute;left:0;right:0;top:14px;font-weight:400;font-size:13.5px;letter-spacing:.4px;color:var(--cyan)}
  .contact .line{position:absolute;left:0;right:0;font-size:9px}
  .contact b{font-family:"Montserrat",sans-serif;font-weight:700;font-size:8.6px}
  .line-1{top:36px}
  .line-2{top:51px}
  .gap{display:inline-block;width:10px}
</style>
</head>
<body>
<div class="sheet">

  <div class="abs section-label" style="left:101px;top:92px">Cover Page</div>

  <section class="abs cover">
    <div class="cover-photo" role="img" aria-label="Black and white city skyline with high-rise towers, trees and red light trails of traffic at dusk"></div>
    <div class="cover-band"></div>
    <h1 class="cover-title">Executive<br>Summary Document</h1>
    <div class="brand">velmora</div>
    <div class="brand-claim">Performance matters.</div>
    <div class="cover-tagline">Your service provider for application performance.</div>
  </section>

  <div class="abs section-label" style="left:103px;top:613px">Summary Page</div>

  <section class="panel who">
    <h2>Who we are</h2>
    <p>velmora is the go-to-company in the very specialized area of performance engineering. Whether microservices in the cloud or legacy onpremise: We will show you the added value of load &amp; performance tests, performance tuning or monitoring solutions. In the area of application performance monitoring, we like to work with the enterprise solution from industry leader Tracewise. velmora is Tracewise Premier Partner and therefore amongst an exclusive group of companies in the EMEA region specialized in Tracewise</p>
  </section>

  <section class="panel team">
    <h2>About our team</h2>
    <p>Our performance engineers guide our customers through the whole process of performance testing by providing best practices for test design and test strategies, setting up infrastructure, carrying out performance tests as well as preparing the reporting. If required, our performance engineers go beyond reporting by identifying the actual bottlenecks and even performing code reviews. As we offer to play such an active role in fixing performance defects, all our consultants are well-skilled software engineers</p>
  </section>

  <div class="abs strip-dark"></div>

  <section class="panel services">
    <h2>Our services</h2>
    <span class="svc-num" style="left:60px">01</span>
    <span class="svc-num" style="left:265px">02</span>
    <span class="svc-num" style="left:455px">03</span>
    <div class="service svc-1">
      <h3>Load &amp; Performance Testing</h3>
      <p>An often-neglected necessity to ensure the speed, stability and reliability of your IT applications and digital services. If you expect many users rushing in on your digital roads, performance tests are required to provide the best experience for your customers.</p>
    </div>
    <div class="service svc-2">
      <h3>APM &amp; Observability</h3>
      <p>Follow the experience of users and pinpoint the root-cause of problems as fast as possible in case of an undesired event and get business insights like usage statistics and conversion rates just along the way</p>
    </div>
    <div class="service svc-3">
      <h3>Training &amp; Workshops</h3>
      <p>Enable your own performance testing team by learning innovative approaches such as the automation of quality gates and automate performance feedback or get started with the basic methodology training.</p>
    </div>
  </section>

  <section class="panel customers">
    <h2>VALUED CUSTOMERS</h2>
    <div class="client client-1">NORDVAL</div>
    <div class="client client-2">KAMRA</div>
    <div class="client client-3"><span class="mark"></span>OSTRIA</div>
    <div class="client client-4">STADTNET</div>
    <div class="client client-5">BAUKRAFT</div>
    <div class="client client-6"><span class="mark"></span>Gemeinlink</div>
  </section>

  <section class="panel contact">
    <h2>CONTACT</h2>
    <div class="line line-1"><b>Phone:</b> +43-1-55 01 23 4567<span class="gap"></span><b>Email:</b> office@velmora-it.example<span class="gap"></span><b>Website:</b> www.velmora-it.example</div>
    <div class="line line-2"><b>Linkfolio:</b> www.linkfolio.example/company/velmora</div>
  </section>
  <div class="abs contact-edge"></div>
  <div class="abs strip-light"></div>

</div>
</body>
</html>
```